K&R Security Services PTY. LTD.

Ive just had my logo made and I'm looking for some simple but strong designs for my business cards the company is a security company.

Please use dark colors.

Regards,

Owen Deloit

Reason: Need more time for discussion with other directors

Industry/Entity Type

Security

Font styles to use
Sans Serif
Decorative

```html
<!DOCTYPE html>
<html lang="en">
<head>
<meta charset="utf-8">
<title>K&amp;R Security Services – Business Cards</title>
<link rel="stylesheet" href="https://fonts.googleapis.com/css2?family=Alegreya+Sans:wght@400;500&display=swap">
<style>
  :root {
    --backdrop: #1d1e21;
    --card: #ffffff;
    --ink: #111111;
    --ink-soft: #3a3a3a;
    --ghost: #d6d6d6;
    --ornament: #1a1a1a;
  }
  * { margin: 0; padding: 0; box-sizing: border-box; }
  html, body { width: 1200px; height: 1000px; overflow: hidden; }
  body {
    background: var(--backdrop);
    font-family: "Alegreya Sans", sans-serif;
    position: relative;
  }
  .business-card {
    position: absolute;
    top: 350px;
    width: 520px;
    height: 300px;
    background: var(--card);
    border-radius: 10px;
    box-shadow: 0 12px 30px rgba(0,0,0,.55);
    overflow: hidden;
  }
  .card-front { left: 60px; }
  .card-back { left: 620px; }

  .brand-block {
    position: absolute;
    left: 40px;
    top: 95px;
    width: 190px;
    display: flex;
    align-items: flex-start;
    gap: 10px;
    color: var(--ink-soft);
    font-weight: 500;
    font-size: 20px;
    line-height: 1.15;
  }
  .brand-mark {
    flex: 0 0 14px;
    width: 14px;
    height: 14px;
    margin-top: 4px;
    background: var(--ink-soft);
  }

  .divider {
    position: absolute;
    left: 262px;
    top: 36px;
    width: 24px;
    height: 228px;
  }

  .contact-block {
    position: absolute;
    left: 308px;
    top: 108px;
    width: 190px;
    color: var(--ink);
  }
  .contact-name {
    font-size: 24px;
    font-weight: 500;
    margin-bottom: 12px;
  }
  .contact-line {
    font-size: 17px;
    font-weight: 400;
    margin-bottom: 10px;
    white-space: nowrap;
  }

  .back-brand {
    position: absolute;
    inset: 0;
    display: flex;
    align-items: center;
    justify-content: center;
    gap: 12px;
    color: var(--ghost);
    font-weight: 500;
    font-size: 26px;
    text-align: center;
  }
  .back-brand .brand-mark { background: var(--ghost); margin-top: 0; }
</style>
</head>
<body>
  <section class="business-card card-front">
    <div class="brand-block">
      <span class="brand-mark"></span>
      <span class="brand-name">K&amp;R Security Services PTY. LTD.</span>
    </div>

    <svg class="divider" viewBox="0 0 24 228">
      <rect role="img" aria-label="fleur-de-lis ornament" x="5" y="0" width="14" height="18" rx="3" fill="var(--ornament)"/>
      <line x1="12" y1="20" x2="12" y2="208" stroke="var(--ornament)" stroke-width="1.5"/>
      <rect role="img" aria-label="fleur-de-lis ornament" x="5" y="210" width="14" height="18" rx="3" fill="var(--ornament)"/>
    </svg>

    <div class="contact-block">
      <p class="contact-name">Owen Deloit</p>
      <p class="contact-line">0140 228 617</p>
      <p class="contact-line">owen@krsecure.example</p>
    </div>
  </section>

  <section class="business-card card-back">
    <div class="back-brand">
      <span class="brand-mark"></span>
      <span class="brand-name">K&amp;R Security Services<br>PTY. LTD.</span>
    </div>
  </section>
</body>
</html>
```